Business Card Design Project

Hello- I am an interior stylist/product designer whose work is detail driven, very clean and transitional in style and I want my business card to reflect those qualities. I have a logo that I use on my website- my name and a hand drawn chandelier that I want incorporated into the design. However, "Design for the Home" needs to be changed to "Designs". I will be using cream colored stock and am thinking of gray text and logo. I need your help in pulling my card together since it will be the most used element and drive the design of the rest of my stationary suite.
Updates

Please note that I have changed my QR code from my cell # to my website. The new code will be downloaded now.

Reason: I want to thank everyone who has submitted designs- there are truly some very inspiring designs and I am very pleased. I want to make certain that I get this right and have an attractive and highly effective marketing tool when we are finished. With that said, I have run into a technical problem with one aspect of the card- a qr code for my website that was not part of the original brief. I will get that corrected today and post. Once I get that taken care of, I will post comments to all designs received do far. Thanks again for everyone's efforts, Risa

QR Code for the website is now uploaded. Thanks for your patience!

Target Market(s)

Upper middle class- mostly women

Industry/Entity Type

Business

Requirements
Must have
• Marisa Vantry Designs
"...to the last detail."
214-555-0148
marisavantry@plumwick.net
www.marisavantrydesigns-example.com
27083 Birchmont Court
Dallas, TX 75000
Nice to have
• Risa Vantry
Owner

```html
<!DOCTYPE html>
<html lang="en">
<head>
<meta charset="utf-8">
<title>Marisa Vantry Designs — Business Card</title>
<link href="https://fonts.googleapis.com/css2?family=Cormorant+Garamond:wght@500&family=Didact+Gothic&display=swap" rel="stylesheet">
<style>
  :root {
    --backdrop: #4d4d4d;
    --card: #f2f2f2;
    --band: #e9e9e9;
    --pattern: #e4e4e4;
    --pattern-light: #efefef;
    --ink: #6a6a6a;
    --ink-soft: #8c8c8c;
  }
  html, body {
    margin: 0;
    padding: 0;
    overflow: hidden;
  }
  .canvas {
    position: relative;
    width: 1200px;
    height: 534px;
    background: var(--backdrop);
    overflow: hidden;
  }
  .card {
    position: absolute;
    top: 117px;
    width: 524px;
    height: 300px;
    border-radius: 22px;
    background: var(--card);
    overflow: hidden;
  }
  .card--front { left: 63px; }
  .card--back { left: 621px; }

  .pattern-band {
    position: absolute;
    left: 0;
    width: 100%;
    height: 88px;
    background: linear-gradient(180deg, var(--pattern), var(--pattern-light) 50%, var(--pattern));
  }
  .pattern-band--top { top: 0; }
  .pattern-band--bottom { bottom: 0; }
  .name-band {
    position: absolute;
    top: 88px;
    left: 0;
    width: 100%;
    height: 124px;
    background: var(--band);
  }

  .wordmark {
    position: absolute;
    text-align: center;
  }
  .card--front .wordmark { left: 0; width: 100%; top: 134px; }
  .card--back .wordmark { left: 20px; width: 235px; top: 134px; }
  .wordmark__name {
    display: block;
    font-family: "Cormorant Garamond", serif;
    font-weight: 500;
    font-size: 36px;
    line-height: 36px;
    color: var(--ink);
  }
  .wordmark__tagline {
    display: block;
    margin-top: 6px;
    font-family: "Didact Gothic", sans-serif;
    font-size: 9.5px;
    line-height: 11px;
    letter-spacing: 1.6px;
    color: var(--ink-soft);
  }
  .wordmark__motto {
    display: block;
    margin-top: 5px;
    font-family: "Cormorant Garamond", serif;
    font-weight: 500;
    font-size: 12px;
    line-height: 13px;
    color: var(--ink-soft);
  }

  .contact {
    position: absolute;
    left: 261px;
    top: 109px;
    font-family: "Didact Gothic", sans-serif;
    color: var(--ink-soft);
    font-size: 10px;
    line-height: 12px;
  }
  .contact__name {
    font-size: 13px;
    line-height: 15px;
    color: var(--ink);
    margin: 0;
  }
  .contact__role { margin: 0 0 6px; }
  .contact__address { margin: 0 0 6px; font-style: normal; }
  .contact__lines { margin: 0; }
</style>
</head>
<body>
<main class="canvas">
  <section class="card card--front" aria-label="Card front">
    <div class="pattern-band pattern-band--top" role="img" aria-label="Light grey repeating chandelier damask pattern"></div>
    <div class="name-band"></div>
    <div class="wordmark">
      <span class="wordmark__name">Marisa Vantry</span>
      <span class="wordmark__tagline">DESIGNS</span>
      <span class="wordmark__motto">...to the last detail.</span>
    </div>
    <div class="pattern-band pattern-band--bottom" role="img" aria-label="Light grey repeating chandelier damask pattern"></div>
  </section>

  <section class="card card--back" aria-label="Card back">
    <div class="wordmark">
      <span class="wordmark__name">Marisa Vantry</span>
      <span class="wordmark__tagline">DESIGNS</span>
      <span class="wordmark__motto">...to the last detail.</span>
    </div>
    <div class="contact">
      <p class="contact__name">Risa Vantry</p>
      <p class="contact__role">Owner</p>
      <address class="contact__address">27083 Birchmont Court<br>Dallas, TX 75000</address>
      <p class="contact__lines">p: 214-555-0148 &nbsp; e: marisavantry@plumwick.net<br>w: www.marisavantrydesigns-example.com</p>
    </div>
  </section>
</main>
</body>
</html>
```